Heavy Equipment Rental Company Looking for Attractive Sign Design

We need a new sign for our forklift rental company in Southern California called Ridgeline Lift Outfitters. We also sell, service and move forklifts and other equipment, but forklift rentals are our main business. Our old sign on the street is deteriorating quickly. I've attached a photo of the old sign - it is approximately 52" high and 48" wide, but may be made 6" or so taller if needed. The old sign is included more to reference the information than the design - the old design definitely has issues (no ArtMarketry at the time). The smaller sign reading Pellworth dealer is not needed. We want the sign to be simple, clean and easy to read, but of course also attractive and professional. We would like the same information on it as is on the previous sign, but it may be re-arranged. The number 3100 is the street number. Here are the essential elements:
3100 (street number)
Ridgeline Lift Outfitters (business name)
714-382-6047 (phone)
www.ridgelineliftco.example (website)
Forklift Rentals and Sales (main businesses)
If possible, we would like the names of our 2 primary brands:
Pellworth and Varnecki Forklifts
Although, if there's no way to implement them nicely, then we can leave them off.

Target Market(s)

Industrial, Construction

Industry/Entity Type

Construction

Colors
0355a3

Requirements
Must have
• Bold, clean, easy to read, with the necessary information.
Nice to have
• Our main machines are all painted blue, so some blue in the design would be nice. In our industry, Pellworth forklifts and Varnecki forklifts are two different brands but have good reputations. It would be nice if we can include them in the design, although a nice design is more important than including the brand names.
Should not have
• Small or difficult to read text. Colors or fonts that are too playful.

```html
<!DOCTYPE html>
<html lang="en">
<head>
<meta charset="utf-8">
<title>Ridgeline Lift Outfitters – Street Sign</title>
<link rel="stylesheet" href="https://fonts.googleapis.com/css2?family=Jost:wght@500;600;700;800&display=swap">
<style>
  :root {
    --brand-blue: #0c55a5;
    --sign-white: #f4f6f5;
    --ink-white: #ffffff;
    --accent-yellow: #ffe600;
    --accent-amber: #fdb913;
    --accent-orange: #f15a29;
    --backdrop: #d9dbdc;
  }
  html, body {
    margin: 0;
    padding: 0;
    width: 1200px;
    height: 1200px;
    overflow: hidden;
    background: var(--backdrop);
  }
  .canvas {
    width: 1200px;
    height: 1200px;
    display: flex;
    align-items: center;
    justify-content: center;
  }
  .sign {
    width: 760px;
    height: 1140px;
    display: block;
    font-family: "Jost", "Futura", sans-serif;
  }
  .sign-face { fill: var(--sign-white); }
  .blue-field { fill: var(--brand-blue); }
  .street-number {
    fill: var(--ink-white);
    font-weight: 700;
    font-size: 230px;
  }
  .business-name {
    fill: var(--ink-white);
    font-weight: 700;
  }
  .name-top { font-size: 88px; }
  .name-main { font-size: 215px; }
  .name-bottom { font-size: 62px; letter-spacing: 16px; }
  .service-line {
    fill: var(--brand-blue);
    font-weight: 700;
    font-size: 64px;
  }
  .phone-number {
    fill: var(--brand-blue);
    font-weight: 600;
    font-size: 122px;
  }
  .web-address {
    fill: var(--brand-blue);
    font-weight: 600;
    font-size: 46px;
  }
  .icon-ring { fill: var(--accent-orange); }
  .icon-core { fill: var(--accent-amber); }
  .icon-line { fill: none; stroke: var(--ink-white); stroke-width: 4; stroke-linecap: round; }
  .icon-fill { fill: var(--ink-white); }
</style>
</head>
<body>
<main class="canvas">
  <svg class="sign" viewBox="0 0 920 1380" role="img" aria-label="Ridgeline Lift Outfitters street sign, number 3100">
    <defs>
      <linearGradient id="swoosh-top" x1="0" y1="0" x2="1" y2="0">
        <stop offset="0" stop-color="var(--accent-yellow)"/>
        <stop offset="0.5" stop-color="var(--accent-amber)"/>
        <stop offset="1" stop-color="var(--accent-orange)"/>
      </linearGradient>
      <linearGradient id="swoosh-bottom" x1="0" y1="0" x2="1" y2="0">
        <stop offset="0" stop-color="var(--accent-orange)"/>
        <stop offset="0.5" stop-color="var(--accent-amber)"/>
        <stop offset="1" stop-color="var(--accent-yellow)"/>
      </linearGradient>
    </defs>

    <!-- sign board with wavy top edge -->
    <path class="sign-face" d="M0,48 C250,-20 500,30 720,95 C820,118 880,80 920,50 L920,1380 L0,1380 Z"/>

    <!-- blue header field -->
    <path class="blue-field" d="M0,48 C250,-20 500,30 720,95 C820,118 880,80 920,50 L920,845 C820,900 720,900 600,870 C420,820 200,760 0,850 Z"/>

    <!-- accent swooshes -->
    <path d="M0,272 C160,210 320,230 480,280 C640,330 780,355 920,275 L920,290 C780,372 640,350 480,300 C320,250 160,235 0,290 Z" fill="url(#swoosh-top)"/>
    <path d="M0,845 C200,755 420,815 600,865 C720,895 820,895 920,840 L920,858 C820,912 720,915 600,885 C420,835 200,775 0,865 Z" fill="url(#swoosh-bottom)"/>

    <!-- street number -->
    <text class="street-number" x="460" y="235" text-anchor="middle" transform="rotate(9 460 160)">3100</text>

    <!-- business name -->
    <text class="business-name name-top" x="70" y="428">RIDGELINE</text>
    <text class="business-name name-main" x="60" y="650">LIFT</text>
    <text class="business-name name-bottom" x="855" y="762" text-anchor="end">OUTFITTERS</text>

    <!-- services -->
    <text class="service-line" x="60" y="1040" textLength="800" lengthAdjust="spacingAndGlyphs">FORKLIFT RENTALS AND SALES</text>

    <!-- phone -->
    <g class="phone-icon" transform="translate(107 1147)">
      <circle class="icon-ring" r="37"/>
      <circle class="icon-core" r="27"/>
      <circle class="icon-line" r="20"/>
      <path class="icon-fill" d="M-9,-12 L-4,-12 L-1,-5 L-5,-2 C-3,3 -1,5 3,6 L6,2 L12,5 L12,10 C12,13 9,14 6,14 C-4,12 -13,3 -14,-7 C-14,-10 -12,-12 -9,-12 Z"/>
    </g>
    <text class="phone-number" x="180" y="1185" textLength="675" lengthAdjust="spacingAndGlyphs">714-382-6047</text>

    <!-- website -->
    <g class="web-icon" transform="translate(107 1267)">
      <circle class="icon-ring" r="37"/>
      <circle class="icon-core" r="27"/>
      <circle class="icon-line" r="19"/>
      <ellipse class="icon-line" rx="8" ry="19"/>
      <line class="icon-line" x1="-19" y1="0" x2="19" y2="0"/>
      <line class="icon-line" x1="0" y1="-19" x2="0" y2="19"/>
      <line class="icon-line" x1="-16" y1="-9" x2="16" y2="-9"/>
      <line class="icon-line" x1="-16" y1="9" x2="16" y2="9"/>
    </g>
    <text class="web-address" x="172" y="1283" textLength="680" lengthAdjust="spacingAndGlyphs">www.ridgelineliftco.example</text>
  </svg>
</main>
</body>
</html>
```